Fontenot Bayou Grillhouse (Owners Card)

Need a classy, but modern business card. I have included a promotional card for the steakhouse. I need one for myself (the owner) that is more professional.

Target Market(s)

General Public

Industry/Entity Type

Food service

Contact Information for Business Card

Name, business address, phone number, email, logo

Font styles to use
Serif
Sans Serif
Decorative
Script

Requirements
Must have
• My name (Darvel Pruitt), business address (327 Oakmere Street), phone number (510) 493-2615, email (Dpruittkr4@mailvane.example. On the back of the card: Psalms 27 1 The LORD is my light and my salvation— whom shall I fear? The LORD is the stronghold of my life— of whom shall I be afraid? 2 When the wicked advance against me to devour me, it is my enemies and my foes who will stumble and fall. 3 Though an army besiege me, my heart will not fear; though war break out against me, even then I will be confident.
Nice to have
• Something that’s bold, but modern and professional.

```html
<!DOCTYPE html>
<html lang="en">
<head>
<meta charset="utf-8">
<title>Fontenot Bayou Grillhouse – Owner Business Card</title>
<link href="https://fonts.googleapis.com/css2?family=Montserrat:wght@400;500;700&display=swap" rel="stylesheet">
<style>
  :root {
    --backdrop: #e9e4dc;
    --card-white: #ffffff;
    --green: #9bc43a;
    --orange: #f39c1f;
    --red: #e8262b;
    --ink: #1b1b1b;
    --text-white: #ffffff;
  }
  * { margin: 0; padding: 0; box-sizing: border-box; }
  html, body { width: 900px; height: 1200px; overflow: hidden; }
  body {
    background: var(--backdrop);
    font-family: "Montserrat", Arial, sans-serif;
    position: relative;
  }
  .card {
    position: absolute;
    border-radius: 24px;
    overflow: hidden;
    box-shadow: 0 6px 14px rgba(0,0,0,0.25);
  }
  /* Front */
  .card-front {
    left: 80px; top: 131px; width: 742px; height: 441px;
    background: var(--card-white);
  }
  .card-front .edge-band {
    position: absolute; left: 0; right: 0; bottom: 0; height: 16px;
    background: linear-gradient(90deg, var(--red), var(--orange) 55%, var(--green));
  }
  .brand-mark {
    position: absolute; left: 70px; top: 200px; width: 260px;
    text-align: center;
    font-weight: 700; font-size: 27px; line-height: 1.2;
    color: var(--red);
  }
  .divider {
    position: absolute; left: 359px; top: 134px; width: 2px; height: 211px;
    background: var(--orange);
  }
  .contact {
    position: absolute; left: 370px; top: 130px;
    color: var(--ink);
  }
  .contact .name { font-size: 25px; font-weight: 700; line-height: 1.2; }
  .contact .name .first { color: var(--green); }
  .contact .name .last { color: var(--red); }
  .contact .role { font-size: 15px; margin-top: 1px; }
  .contact .address { font-size: 16px; line-height: 1.3; margin: 22px 0 0 2px; }
  .contact .lines { list-style: none; margin: 16px 0 0 4px; font-size: 15.5px; }
  .contact .lines li { display: flex; align-items: center; height: 27px; }
  .contact .lines svg { width: 15px; height: 15px; margin-right: 12px; flex: none; }
  /* Back */
  .card-back {
    left: 78px; top: 638px; width: 744px; height: 440px;
    background: linear-gradient(90deg, var(--green) 0%, var(--orange) 45%, var(--orange) 55%, var(--red) 100%);
  }
  .card-back .brand-mark {
    left: 150px; top: 150px; width: 444px;
    font-size: 40px; color: var(--ink);
  }
  .scripture {
    position: absolute; left: 37px; top: 308px; width: 660px;
    color: var(--text-white);
    font-weight: 700; font-size: 15.5px; line-height: 1.45;
    padding-left: 14px; text-indent: -14px;
  }
</style>
</head>
<body>
  <section class="card card-front">
    <div class="brand-mark">Fontenot Bayou Grillhouse</div>
    <div class="divider"></div>
    <div class="contact">
      <h1 class="name"><span class="first">Darvel</span> <span class="last">Pruitt</span></h1>
      <p class="role">Owner</p>
      <p class="address">327 Oakmere Street<br>Brennerton, CA&nbsp; 94571</p>
      <ul class="lines">
        <li>
          <svg viewBox="0 0 16 16"><path fill="#9bc43a" d="M3.5 1.5l2.5 2.8-1.3 1.6c.9 2 2.4 3.5 4.4 4.4l1.6-1.3 2.8 2.5-1.4 2.2C7 13.2 2.8 9 1.3 3z"/></svg>
          (510) 493-2615
        </li>
        <li>
          <svg viewBox="0 0 16 16"><rect x="1" y="3.5" width="14" height="9.5" fill="#f39c1f"/><path d="M1 3.5l7 5 7-5" fill="none" stroke="#fff" stroke-width="1.2"/></svg>
          Dpruittkr4@mailvane.example
        </li>
        <li>
          <svg viewBox="0 0 16 16"><circle cx="8" cy="8" r="7" fill="#e8262b"/><path d="M1 8h14M8 1c-3 3-3 11 0 14M8 1c3 3 3 11 0 14" fill="none" stroke="#fff" stroke-width="1"/></svg>
          www.Fontbayou.example
        </li>
      </ul>
    </div>
    <div class="edge-band"></div>
  </section>

  <section class="card card-back">
    <div class="brand-mark">Fontenot Bayou Grillhouse</div>
    <p class="scripture">1 The LORD is my light and my salvation– whom shall I fear? The LORD is the stronghold of my life– of whom shall I be afraid? 2 When the wicked advance against me to devour me, it is my enemies and my foes who will stumble and fall <sup>3</sup> Though an army besiege me, my heart will not fear; though war break out against me, even then I will be confident.</p>
  </section>
</body>
</html>
```